Postcard design for Intellectual Property Professional Conference

Seeking design for 5.5" by 8.5" postcard mailer about a conference on tax and finance issues for international IP management. Attendees are lawyers and financial executives. Draft language is attached.

Target Market(s)

The project should have the attached picture of Boston with the caption "Courtesy of the Harborline Meeting & Travelers Council"

Industry/Entity Type

Finance

```html
<!DOCTYPE html>
<html lang="en">
<head>
<meta charset="utf-8">
<title>Increasing Profits &amp; Protecting Intellectual Property — Conference Postcard</title>
<link href="https://fonts.googleapis.com/css2?family=Bebas+Neue&family=Source+Sans+3:wght@400;600;700&display=swap" rel="stylesheet">
<style>
  :root {
    --blue: #1ba3e6;
    --navy: #0d2a4b;
    --ink: #1f2f45;
    --paper: #ffffff;
    --backdrop: #6b6c6e;
    --photo-a: #c9d3dd;
    --photo-b: #eef2f6;
  }
  * { box-sizing: border-box; margin: 0; padding: 0; }
  html, body { width: 1200px; height: 850px; overflow: hidden; }
  body { background: var(--backdrop); position: relative; font-family: "Source Sans 3", Arial, sans-serif; }

  .postcard {
    position: absolute; left: 60px; top: 75px;
    width: 1080px; height: 700px;
    background: var(--paper); overflow: hidden;
  }
  .shapes { position: absolute; inset: 0; }

  .headline {
    position: absolute; left: 41px; top: 26px;
    font-family: "Bebas Neue", Impact, sans-serif;
    font-size: 49px; line-height: 46px; letter-spacing: 0.2px;
    color: var(--navy); font-weight: 400;
  }
  .headline .accent { color: var(--blue); }

  .event-info {
    position: absolute; left: 846px; top: 38px;
    font-family: "Bebas Neue", Impact, sans-serif;
    font-size: 31px; line-height: 32px; color: var(--paper);
  }

  .invitation {
    position: absolute; left: 45px; top: 161px; width: 510px;
    color: var(--paper); font-size: 16px; line-height: 17.7px;
  }
  .invitation p + p { margin-top: 18px; }

  .photo-caption {
    position: absolute; left: 596px; top: 434px;
    font-size: 11px; color: var(--navy); letter-spacing: 0.2px;
  }

  .topics-label {
    position: absolute; left: 72px; top: 437px;
    color: var(--paper); font-weight: 700; font-size: 17px; letter-spacing: 1.2px;
  }

  .topics { position: absolute; top: 478px; width: 300px; list-style: none;
    color: var(--ink); font-size: 14px; line-height: 17.5px; }
  .topics li { position: relative; padding-left: 17px; margin-bottom: 6px; }
  .topics li::before {
    content: ""; position: absolute; left: 0; top: 4px;
    border-left: 9px solid var(--blue);
    border-top: 5px solid transparent; border-bottom: 5px solid transparent;
  }
  .topics li.continued::before { display: none; }
  .topics-col-1 { left: 53px; width: 300px; }
  .topics-col-2 { left: 388px; width: 305px; }
  .topics-col-3 { left: 722px; width: 300px; }

  .register {
    position: absolute; left: 55px; top: 654px;
    font-family: "Bebas Neue", Impact, sans-serif;
    font-size: 34px; color: var(--paper); letter-spacing: 0.3px;
  }
  .website {
    position: absolute; right: 43px; top: 656px;
    font-weight: 700; font-size: 20px; color: var(--navy);
  }
</style>
</head>
<body>
  <article class="postcard">
    <svg class="shapes" width="1080" height="700" viewBox="0 0 1080 700">
      <polygon points="826,20 1080,20 1080,116 806,116" fill="var(--blue)"/>
      <rect x="0" y="138" width="1080" height="315" fill="var(--navy)"/>
      <polygon points="622,138 646,138 556,453 532,453" fill="var(--blue)"/>
      <defs>
        <linearGradient id="photoTone" x1="0" y1="0" x2="1" y2="1">
          <stop offset="0" stop-color="var(--photo-b)"/>
          <stop offset="1" stop-color="var(--photo-a)"/>
        </linearGradient>
      </defs>
      <polygon role="img" aria-label="Photo of the Boston skyline"
               points="646,138 1080,138 1080,190 1010,453 556,453" fill="url(#photoTone)"/>
      <polygon points="1080,190 1080,260 1028,453 1010,453" fill="var(--navy)"/>
      <polygon points="1080,230 1080,270 1034,453 1020,453" fill="var(--blue)"/>
      <polygon points="50,427 405,427 392,468 40,468" fill="var(--blue)"/>
      <polygon points="0,647 481,647 468,700 0,700" fill="var(--blue)"/>
    </svg>

    <h1 class="headline">
      <span class="accent">Increasing Profits &amp; Protecting</span> Intellectual<br>
      Property in Developing Growth Markets
    </h1>

    <div class="event-info">Boston<br>March 24 &amp; 25, 2016</div>

    <div class="invitation">
      <p>You are cordially invited to attend a comprehensive and practical day and a half conference to examine the tax and legal structuring strategies for increasing profits from Intellectual properties while protecting these important assets when doing business in fast growing developing markets. Intellectual property assets include some of the most important assets of most companies: their patents, trade marks, copyrights, brand names and licensing agreements.</p>
      <p>Senior tax, legal and financial experts will provide a comprehensive analysis of the legal issues, recent tax &amp; regulatory developments, skills and structuring strategies necessary to maximize profits from IP Migrating IP assets to low tax jurisdiction will also be covered along with dealing with issues of piracy, counterfeiting, infringement and other legal challenges to a company’s IP.</p>
    </div>

    <div class="photo-caption">Courtesy of the Harborline Meeting &amp; Travelers Council</div>

    <div class="topics-label">TOPICS TO BE COVERED INCLUDE:</div>

    <ul class="topics topics-col-1">
      <li>Market trends in IP tax &amp; legal structures</li>
      <li>Proposed US Tax changes and regulatory developments outside the US including European and OECD developments affecting IP, patent box, base erosion and profit splitting (BEPS)</li>
      <li>Overview of the IP landscape in key developing growth markets such as China, India, Brazil,</li>
    </ul>
    <ul class="topics topics-col-2">
      <li class="continued">Korea, South Africa, Mexico and other developing markets outside the US.</li>
      <li>Legal issues including litigation, arbitration and use of government assistance to protect IP values in key developing markets.</li>
      <li>Monetizing IP assets and rights in regard to divestitures, spin offs, split offs, M&amp;A, transfers of ownership and securitizations in developing</li>
    </ul>
    <ul class="topics topics-col-3">
      <li class="continued">growth markets</li>
      <li>Special Tax Planning and Legal Considerations for IP in Particular Sectors such as Biopharmaceutical, International Sports Licensing, High Tech, Consumer Brands, and Manufacuring</li>
      <li>Restructuring and Migration of IP Assets to Tax Advantaged Jurisdictions</li>
    </ul>

    <div class="register">Register Early and Save up to $300</div>
    <div class="website">www.harborlineforums.com</div>
  </article>
</body>
</html>
```